New Company Business Card Design

I have a new company logo and I want a new business card design. I dont know if the logo file i attached is in the correct format or quality. We are a New York City Specialty construction Firm specializing in high risk out of the box projects. I want a simple and classy business card that people will his card is as crisp as the work his company does.

Target Market(s)

Clients in the heavy construction industry in New York City

Industry/Entity Type

Construction Company

Contact Information for Business Card

Simple Classy - DIFFERENT

Font styles to use
Other font styles liked:
• Mach the logo font in some way

Colors

Designer to choose colors to be used in the design.

Requirements
Must have
• Uniqueness
Nice to have
• Nothing particular - Just different and classy - Timeless
Should not have
• Goofy Shit or Gimmicky shit

```html
<!DOCTYPE html>
<html lang="en">
<head>
<meta charset="utf-8">
<title>KRV Builders – Business Card</title>
<link href="https://fonts.googleapis.com/css2?family=Sorts+Mill+Goudy&display=swap" rel="stylesheet">
<style>
  :root {
    --ink: #000000;
    --paper: #ffffff;
    --brand-blue: #1d9bd8;
    --bright-blue: #27aae1;
    --deep-blue: #0e3a52;
    --ghost-blue: rgba(39,170,225,0.10);
    --ghost-grey: rgba(0,0,0,0.13);
  }
  * { margin: 0; padding: 0; box-sizing: border-box; }
  html, body { width: 971px; height: 1200px; overflow: hidden; background: var(--paper); }
  body { position: relative; font-family: "Sorts Mill Goudy", Georgia, serif; font-variant-numeric: lining-nums; }

  .backdrop { position: absolute; inset: 0; }

  .wordmark {
    position: absolute; display: flex; align-items: center; gap: 12px;
    color: var(--brand-blue); white-space: nowrap; line-height: 1;
  }
  .wordmark .mark-square { background: var(--brand-blue); flex: none; }
  .wordmark--front {
    left: 69px; top: 298px; width: 350px; justify-content: center;
    transform: translateY(-50%); font-size: 36px;
  }
  .wordmark--front .mark-square { width: 20px; height: 20px; }

  .card { position: absolute; background: var(--ink); overflow: hidden; }
  .card-front { left: 459px; top: 21px; width: 487px; height: 551px; }
  .card-back  { left: 26px;  top: 627px; width: 918px; height: 551px; }
  .card-deco { position: absolute; inset: 0; }

  .pixel-strip {
    position: absolute; left: 0; top: -14px; width: 35px;
    display: grid; grid-template-columns: 18px 17px; grid-auto-rows: 17px;
  }

  .holder-name {
    position: absolute; left: 93px; top: 130px;
    font-size: 49px; line-height: 1; color: var(--paper); font-weight: 400; white-space: nowrap;
  }
  .holder-name .accent { color: var(--brand-blue); }

  .contact-list { position: absolute; left: 93px; top: 0; list-style: none; color: var(--paper); font-size: 21px; line-height: 29px; }
  .contact-item { position: absolute; left: 0; display: flex; align-items: center; white-space: nowrap; }
  .contact-icon { width: 33px; height: 33px; border-radius: 50%; background: var(--bright-blue); flex: none; display: flex; align-items: center; justify-content: center; }
  .contact-icon svg { width: 18px; height: 18px; }
  .contact-text { margin-left: 17px; }
  .item-phone { top: 284px; }
  .item-phone .contact-text { text-align: right; }
  .item-mail { top: 357px; }
  .item-place { top: 422px; align-items: flex-start; }
  .item-place .contact-icon { margin-top: -2px; }
  .item-place .contact-text { text-align: center; }
  .item-web { top: 482px; }

  .wordmark--back {
    left: 50%; top: 50%; transform: translate(-50%, -50%); font-size: 52px;
  }
  .wordmark--back .mark-square { width: 28px; height: 28px; }

  .trail-square { position: absolute; width: 15px; height: 15px; }
  .trail-line { position: absolute; background: var(--bright-blue); }
</style>
</head>
<body>

<svg class="backdrop" width="971" height="1200" aria-hidden="true">
  <line x1="630" y1="560" x2="575" y2="620" stroke="var(--ghost-grey)" stroke-width="22"/>
  <line x1="820" y1="470" x2="695" y2="625" stroke="rgba(14,90,130,0.28)" stroke-width="22"/>
  <line x1="0" y1="1150" x2="30" y2="1120" stroke="var(--ghost-blue)" stroke-width="28"/>
  <line x1="60" y1="1200" x2="90" y2="1170" stroke="var(--ghost-blue)" stroke-width="28"/>
</svg>

<div class="wordmark wordmark--front"><span class="mark-square"></span>KRV Builders, Inc.</div>

<section class="card card-front">
  <svg class="card-deco" width="487" height="551" aria-hidden="true">
    <polyline points="260,520 410,370 530,490" fill="none" stroke="rgba(14,58,82,0.35)" stroke-width="26" stroke-linecap="round" stroke-linejoin="round"/>
    <line x1="410" y1="420" x2="250" y2="580" stroke="rgba(39,170,225,0.28)" stroke-width="22"/>
  </svg>

  <div class="pixel-strip" aria-hidden="true">
    <span style="background:#d9eef9"></span><span style="background:#0b1d27"></span>
    <span style="background:#e6f4fb"></span><span style="background:#08141b"></span>
    <span style="background:#b8e0f4"></span><span style="background:#0d2c3c"></span>
    <span style="background:#cfe9f7"></span><span style="background:#10344a"></span>
    <span style="background:#000"></span><span style="background:#000"></span>
    <span style="background:#a6d8f1"></span><span style="background:#123b52"></span>
    <span style="background:#8fd0ee"></span><span style="background:#165a7c"></span>
    <span style="background:#c2e5f6"></span><span style="background:#0f3146"></span>
    <span style="background:#7cc8ec"></span><span style="background:#1a6b92"></span>
    <span style="background:#9dd5f0"></span><span style="background:#122f40"></span>
    <span style="background:#6fc2ea"></span><span style="background:#1b6d96"></span>
    <span style="background:#55b8e6"></span><span style="background:#1e7aa6"></span>
    <span style="background:#000"></span><span style="background:#000"></span>
    <span style="background:#7fcaec"></span><span style="background:#1c5f80"></span>
    <span style="background:#5cbbe7"></span><span style="background:#1f84b3"></span>
    <span style="background:#93d2ef"></span><span style="background:#133a50"></span>
    <span style="background:#000"></span><span style="background:#000"></span>
    <span style="background:#3fb0e3"></span><span style="background:#2189ba"></span>
    <span style="background:#37ade2"></span><span style="background:#2aa6dd"></span>
    <span style="background:#4ab4e4"></span><span style="background:#1c6f97"></span>
    <span style="background:#000"></span><span style="background:#000"></span>
    <span style="background:#45b2e4"></span><span style="background:#1f86b6"></span>
    <span style="background:#2fa9df"></span><span style="background:#1a5e80"></span>
    <span style="background:#000"></span><span style="background:#000"></span>
    <span style="background:#2aa7df"></span><span style="background:#1f8fc5"></span>
    <span style="background:#29a8e0"></span><span style="background:#29a8e0"></span>
    <span style="background:#29a8e0"></span><span style="background:#0e3a52"></span>
    <span style="background:#000"></span><span style="background:#000"></span>
    <span style="background:#27aae1"></span><span style="background:#27aae1"></span>
    <span style="background:#27aae1"></span><span style="background:#27aae1"></span>
    <span style="background:#0a93d8"></span><span style="background:#0a93d8"></span>
  </div>

  <h1 class="holder-name">Marcus <span class="accent">T. Ellery</span></h1>

  <ul class="contact-list">
    <li class="contact-item item-phone">
      <span class="contact-icon"><svg viewBox="0 0 24 24"><path fill="#fff" d="M6.6 10.8a15.1 15.1 0 0 0 6.6 6.6l2.2-2.2a1 1 0 0 1 1-.25 11.4 11.4 0 0 0 3.6.57 1 1 0 0 1 1 1V20a1 1 0 0 1-1 1A17 17 0 0 1 3 4a1 1 0 0 1 1-1h3.5a1 1 0 0 1 1 1c0 1.25.2 2.45.57 3.57a1 1 0 0 1-.25 1z"/></svg></span>
      <span class="contact-text">Company: (555) 014-2270<br>Personal: (555) 017-3841</span>
    </li>
    <li class="contact-item item-mail">
      <span class="contact-icon"><svg viewBox="0 0 24 24"><rect x="3" y="6" width="18" height="12" fill="#fff"/><polyline points="3,6 12,13 21,6" fill="none" stroke="#27aae1" stroke-width="1.6"/></svg></span>
      <span class="contact-text">marcus@krvbuild.com</span>
    </li>
    <li class="contact-item item-place">
      <span class="contact-icon"><svg viewBox="0 0 24 24"><path fill="#fff" d="M12 2a7 7 0 0 0-7 7c0 5 7 13 7 13s7-8 7-13a7 7 0 0 0-7-7zm0 9.5A2.5 2.5 0 1 1 12 6.5a2.5 2.5 0 0 1 0 5z"/></svg></span>
      <span class="contact-text">418 Harbor Line Avenue - Bayonne,<br>New Jersey 07002</span>
    </li>
    <li class="contact-item item-web">
      <span class="contact-icon"><svg viewBox="0 0 24 24"><circle cx="12" cy="12" r="8" fill="none" stroke="#fff" stroke-width="2"/><ellipse cx="12" cy="12" rx="3.5" ry="8" fill="none" stroke="#fff" stroke-width="1.5"/><line x1="4" y1="12" x2="20" y2="12" stroke="#fff" stroke-width="1.5"/></svg></span>
      <span class="contact-text">www.krvbuild.com</span>
    </li>
  </ul>
</section>

<section class="card card-back">
  <svg class="card-deco" width="918" height="551" aria-hidden="true">
    <polyline points="-40,560 240,280 520,560" fill="none" stroke="rgba(14,58,82,0.45)" stroke-width="30" stroke-linecap="round" stroke-linejoin="round"/>
    <line x1="225" y1="400" x2="40" y2="590" stroke="rgba(14,58,82,0.45)" stroke-width="26"/>
  </svg>

  <div class="wordmark wordmark--back"><span class="mark-square"></span>KRV Builders, Inc.</div>

  <span class="trail-square" style="left:64px;top:496px;background:#050c10"></span>
  <span class="trail-square" style="left:90px;top:496px;background:#07141b"></span>
  <span class="trail-square" style="left:116px;top:496px;background:#0a1c27"></span>
  <span class="trail-square" style="left:142px;top:496px;background:#0c2331"></span>
  <span class="trail-square" style="left:168px;top:496px;background:#0e2a3b"></span>
  <span class="trail-square" style="left:194px;top:496px;background:#103246"></span>
  <span class="trail-square" style="left:220px;top:496px;background:#123b52"></span>
  <span class="trail-square" style="left:246px;top:496px;background:#144561"></span>
  <span class="trail-square" style="left:272px;top:496px;background:#175272"></span>
  <span class="trail-square" style="left:298px;top:496px;background:#1a6186"></span>
  <span class="trail-square" style="left:324px;top:496px;background:#1d739f"></span>
  <span class="trail-square" style="left:350px;top:496px;background:#1f86b9"></span>
  <span class="trail-square" style="left:376px;top:496px;background:#1e97d2"></span>
  <span class="trail-square" style="left:402px;top:496px;background:#12a0e0"></span>
  <span class="trail-square" style="left:428px;top:496px;background:#16a3e2"></span>
  <span class="trail-square" style="left:454px;top:496px;background:#1ea7e2"></span>
  <span class="trail-square" style="left:480px;top:496px;background:#27aae1"></span>
  <span class="trail-line" style="left:509px;top:496px;width:376px;height:15px;border-bottom-right-radius:10px"></span>
  <span class="trail-line" style="left:866px;top:262px;width:15px;height:249px;border-bottom-right-radius:10px"></span>

  <span class="trail-square" style="left:866px;top:2px;background:#07141b"></span>
  <span class="trail-square" style="left:866px;top:29px;background:#0a1c27"></span>
  <span class="trail-square" style="left:866px;top:56px;background:#0e2a3b"></span>
  <span class="trail-square" style="left:866px;top:83px;background:#123b52"></span>
  <span class="trail-square" style="left:866px;top:110px;background:#154862"></span>
  <span class="trail-square" style="left:866px;top:137px;background:#175272"></span>
  <span class="trail-square" style="left:866px;top:164px;background:#1c6f97"></span>
  <span class="trail-square" style="left:866px;top:191px;background:#1f86b9"></span>
  <span class="trail-square" style="left:866px;top:218px;background:#0a93d8"></span>
  <span class="trail-square" style="left:866px;top:240px;background:#12a0e0"></span>
</section>

</body>
</html>
```